Create a Brochure Design for Brantley Homecare

Brantley Homecare is a subsidiary of the Brantley Care Group. This brochure is specifically for the Brantley Homecare company and brand. Create a 3 panel, A4, front and back, tri-fold brochure. This brochure will be a way to introduce our Homecare services to the community, prospective clients, and various referral partners. The brochure must be eye catching, unique in its deliverables and demonstrate both attention to detail and comfort. Our organization is sophisticated and built around warmth, care and individualized personal attention. The most important aspect of this design is to focus on creating a nurturing, warm, and inviting feel where you would want to have a Nurse or Nurse’s Aide in your own home or a loved one’s home.

I am open to the creativity of the designer to develop something based on the above criteria; however I would like the design to work well with the existing collateral material. What I mean by that is that while I want everything to have its own personality and stand out as its own brand representative, I still need to be able to tell that the overall design concept stays stylistically inside of the same ‘family’ of existing designed material. Because of this, below I would like for the designer to pull inspiration from the link to our website (Located below) as well as from the attachment of our recently refreshed business cards (Attached). This should allow each design to be unique and creative, while still staying inside of a framework and the feel/style that I am looking for.

Finally, I want all the designers to understand that this brochure design is for a private, in home, healthcare company where we are responsible for providing personalized care for a culturally and ethnically diverse make-up clientele of all ages. The photos that are used must represent an image of warmth, care, and a positive interaction between client and caregiver.

Look under the Brantley Homecare tab at www.brantleycaregroup-example.net

Industry/Entity Type

Healthcare

Requirements
Must have
• • The Brantley Homecare company logo must be included.

```html
<!DOCTYPE html>
<html lang="en">
<head>
<meta charset="utf-8">
<title>Brantley Homecare – Tri-fold Brochure, Inside Spread</title>
<link href="https://fonts.googleapis.com/css2?family=Source+Sans+3:wght@400;600;700&display=swap" rel="stylesheet">
<style>
  :root {
    --page-bg: #ffffff;
    --brand-orange: #f07b55;
    --peach: #f5c08e;
    --care-green: #14864a;
    --mist: #e4eeec;
    --mist-light: #f2f7f6;
    --mist-deep: #c9dcd8;
    --photo-teal: #a9c9c9;
    --photo-skin: #c79a80;
    --white: #ffffff;
  }
  * { box-sizing: border-box; margin: 0; padding: 0; }
  html, body {
    width: 1200px; height: 800px; overflow: hidden;
    background: var(--page-bg);
    font-family: "Source Sans 3", "Myriad Pro", Arial, sans-serif;
  }
  .brochure {
    position: absolute; left: 75px; top: 29px;
    width: 1050px; height: 742px;
    box-shadow: 0 6px 24px rgba(0,0,0,.12);
    overflow: hidden;
    background: var(--mist-light);
  }

  /* Spread photo across the first two panels */
  .spread-photo {
    position: absolute; left: 0; top: 0; width: 700px; height: 560px;
    background:
      linear-gradient(90deg, rgba(242,247,246,0) 0%, rgba(242,247,246,0) 48%, rgba(242,247,246,.82) 60%, rgba(242,247,246,.9) 100%),
      linear-gradient(165deg, var(--mist) 0%, var(--photo-teal) 40%, var(--photo-skin) 75%, #8fb3c6 100%);
  }
  .fold {
    position: absolute; top: 0; bottom: 0; width: 1px;
    background: rgba(0,0,0,.06);
  }
  .fold--one { left: 350px; }
  .fold--two { left: 700px; }

  .brand-mark {
    position: absolute; display: flex; align-items: center; gap: 6px;
    color: var(--brand-orange); font-weight: 700;
  }
  .brand-mark .square { background: var(--brand-orange); display: block; }
  .brand-mark--small { top: 20px; left: 20px; font-size: 14px; }
  .brand-mark--small .square { width: 14px; height: 14px; }

  /* Peach band across panels one and two */
  .care-band { position: absolute; left: 0; top: 430px; width: 700px; height: 312px; }
  .care-band__text {
    position: absolute; left: 36px; top: 488px; width: 620px;
    color: var(--white); font-weight: 600; font-size: 15px; line-height: 1.5;
  }

  .copy {
    position: absolute; color: var(--care-green); font-weight: 700;
    font-size: 14px; line-height: 1.4; text-align: justify;
  }
  .copy p + p { margin-top: 16px; }
  .copy--levels { left: 380px; top: 48px; width: 292px; }

  /* Panel three */
  .panel--schedule {
    position: absolute; left: 700px; top: 0; width: 350px; height: 742px;
    background: linear-gradient(180deg, var(--mist) 0%, var(--mist-light) 45%, #ffffff 100%);
  }
  .brand-block { position: absolute; top: 40px; right: 30px; text-align: right; }
  .brand-block .brand-mark { position: static; justify-content: flex-end; font-size: 24px; }
  .brand-block .brand-mark .square { width: 22px; height: 22px; }
  .tagline { color: var(--care-green); font-size: 11px; font-weight: 600; margin-top: 4px; line-height: 1.2; }
  .copy--schedule { left: 26px; top: 150px; width: 296px; }
  .photo-frame {
    position: absolute; left: 0; right: 0; bottom: 0; height: 250px;
    background: var(--peach); padding: 24px 28px 30px;
  }
  .care-photo {
    width: 100%; height: 100%;
    background: linear-gradient(135deg, #ece6dc 0%, #d7b49c 45%, #c3ccd6 100%);
    box-shadow: 0 2px 6px rgba(0,0,0,.2);
  }
</style>
</head>
<body>
<main class="brochure">

  <div class="spread-photo" role="img" aria-label="Photo of a smiling nurse in a white coat with a stethoscope, beside a faded older client"></div>
  <div class="brand-mark brand-mark--small"><span class="square"></span>Brantley Homecare</div>

  <div class="copy copy--levels">
    <p>Brantley Homecare provides two different levels of care. Our Nurse Care Consultant will assist the client and family in determining the appropriate level of care needed during the complimentary initial consultation.</p>
    <p>Nurse Aide Care – Our Nurse Aides help you with your personal care needs, provide companionship, run errands, and do light housekeeping, along with assisting you with the activities of daily living.</p>
    <p>Skilled Nursing Care – We offer a wide range of skilled nursing services using RN's and LPN's who provide treatment from wound care to IV support, in addition to all of the services performed by our Nurse Aides.</p>
  </div>

  <svg class="care-band" viewBox="0 0 700 312" aria-hidden="true">
    <path d="M0 22 Q350 -18 700 44 L700 312 L0 312 Z" fill="var(--peach)"/>
  </svg>
  <p class="care-band__text">Our Nurse Aides help you perform all of your daily activities. All of our Care Professionals are bonded, insured, and supervised, and they specialize in personal care in the home. Whether you need respite care, palliative care, long-term care, or in-home care, we can help. Be assured that quality, dependable help is just a phone call away. We consider it a privilege to be able to provide care to those in need. Call us to schedule a complimentary initial consultation.</p>

  <section class="panel--schedule">
    <div class="brand-block">
      <div class="brand-mark"><span class="square"></span>Brantley Homecare</div>
      <p class="tagline">Someone you can depend on...<br>Without question.</p>
    </div>
    <div class="copy copy--schedule">
      <p>Brantley Homecare is flexible with your care needs. As you need more or less care, the schedule can be adjusted to accommodate your needs. We have found that a set schedule works best (same days and times each week). This allows you to be able to depend on the same care professional(s) each week. You determine the schedule, from a minimum of four hours per shift to 24 hours of care per day, 7 days per week, 365 days per year. Our Scheduling department is available 24 hours per day.</p>
    </div>
    <div class="photo-frame">
      <div class="care-photo" role="img" aria-label="Photo of a caregiver smiling with an elderly man at home"></div>
    </div>
  </section>

  <div class="fold fold--one"></div>
  <div class="fold fold--two"></div>
</main>
</body>
</html>
```